A4 Flyer to introduce new line of ice cream cakes and dessert in a bakery shop

[The flyer should have written:]

Welcome to our new line of ice-cream desserts.

As everything else, all hand-made in our kitchen only with natural ingredients.

Try our new....

[then three sections with the following products]

* Ice-cream cakes
* Ice-creams
* Cookie ice-creams

Target Market(s)

Families

Industry/Entity Type

Shop

Font styles to use
Other font styles liked:
• Futura

Requirements
Must have
• Please include our logo on the flyer (see file attached)

```html
<!DOCTYPE html>
<html lang="en">
<head>
<meta charset="utf-8">
<title>mielora – new ice-cream desserts flyer</title>
<link rel="stylesheet" href="https://fonts.googleapis.com/css2?family=Jost:ital,wght@0,400;0,500;1,400&display=swap">
<style>
  :root {
    --cream-light: #fbf7ec;
    --cream: #f1e7cd;
    --gold: #c9a13b;
    --gold-dark: #a9821f;
    --gold-light: #e2c36b;
    --brown-text: #8a6a1c;
    --label-text: #5a4312;
    --white: #ffffff;
    --photo-choc: #6b3f22;
    --photo-caramel: #c98a45;
    --photo-cream: #efe2c4;
  }
  html, body {
    margin: 0;
    padding: 0;
    overflow: hidden;
    background: var(--cream-light);
  }
  .flyer {
    position: relative;
    width: 900px;
    height: 1200px;
    overflow: hidden;
    background: radial-gradient(ellipse at 50% 40%, var(--cream-light) 0%, var(--cream) 100%);
    font-family: "Jost", "Futura", sans-serif;
    color: var(--brown-text);
  }
  .pennant {
    position: absolute;
    left: 310px;
    top: 0;
    width: 280px;
    height: 190px;
  }
  .brand {
    position: absolute;
    left: 0;
    right: 0;
    top: 92px;
    text-align: center;
    font-size: 40px;
    font-weight: 400;
    letter-spacing: 1px;
    color: var(--gold-dark);
  }
  .gold-band {
    position: absolute;
    left: 0;
    width: 900px;
    background: linear-gradient(180deg, var(--gold-light) 0%, var(--gold) 55%, var(--gold-dark) 100%);
  }
  .gold-band.top { top: 330px; height: 62px; }
  .feature-frame {
    position: absolute;
    left: 265px;
    top: 185px;
    width: 370px;
    height: 370px;
    border-radius: 50%;
    background: var(--white);
    border: 5px solid var(--gold);
    box-sizing: border-box;
    box-shadow: 0 6px 14px rgba(120, 90, 20, 0.25);
  }
  .photo {
    position: absolute;
    border-radius: 50%;
  }
  .feature-frame .photo {
    left: 18px; top: 18px; right: 18px; bottom: 18px;
    background: radial-gradient(circle at 50% 45%, var(--photo-cream) 0%, var(--photo-caramel) 55%, var(--photo-choc) 100%);
  }
  .welcome {
    position: absolute;
    left: 0; right: 0;
    top: 588px;
    margin: 0;
    text-align: center;
    font-size: 36px;
    font-weight: 400;
    line-height: 1.2;
    color: var(--brown-text);
  }
  .try-new {
    position: absolute;
    left: 350px;
    width: 200px;
    top: 690px;
    margin: 0;
    text-align: center;
    font-size: 44px;
    font-weight: 500;
    line-height: 1.05;
    color: var(--gold-dark);
  }
  .product {
    position: absolute;
    border-radius: 50%;
    background: var(--white);
    border: 4px solid var(--gold);
    box-sizing: border-box;
    box-shadow: 0 5px 12px rgba(120, 90, 20, 0.22);
  }
  .product .photo { left: 12px; top: 12px; right: 12px; bottom: 12px; }
  .product.ice-cream { left: 115px; top: 685px; width: 230px; height: 230px; }
  .product.ice-cream .photo { background: radial-gradient(circle at 45% 40%, #9a6a45 0%, var(--photo-choc) 70%, #3e2414 100%); }
  .product.cookie { left: 555px; top: 680px; width: 220px; height: 220px; }
  .product.cookie .photo { background: linear-gradient(160deg, #2e1c12 0%, #5a3620 45%, var(--photo-cream) 100%); }
  .product.cake { left: 355px; top: 840px; width: 190px; height: 190px; }
  .product.cake .photo { background: radial-gradient(circle at 50% 55%, var(--photo-caramel) 0%, #a8652e 60%, var(--photo-choc) 100%); }
  .label {
    position: absolute;
    padding: 4px 14px;
    background: var(--gold-light);
    border: 2px solid var(--gold);
    border-radius: 16px;
    font-size: 17px;
    line-height: 1.3;
    color: var(--label-text);
    white-space: nowrap;
  }
  .label.ice-cream-label { left: 80px; top: 830px; }
  .label.cookie-label { left: 690px; top: 830px; }
  .label.cake-label { left: 450px; top: 1012px; transform: translateX(-50%); }
  .gold-band.bottom {
    top: 1090px;
    height: 64px;
    display: flex;
    align-items: center;
    justify-content: center;
  }
  .tagline {
    margin: 0;
    font-size: 30px;
    font-style: italic;
    color: var(--white);
  }
</style>
</head>
<body>
<main class="flyer">
  <svg class="pennant" viewBox="0 0 280 190" aria-hidden="true">
    <polygon points="0,0 280,0 280,150 140,190 0,150" fill="#ffffff"/>
    <polyline points="0,150 140,190 280,150" fill="none" stroke="#e6d6a8" stroke-width="2"/>
  </svg>
  <div class="brand">mielora</div>

  <div class="gold-band top"></div>
  <div class="feature-frame">
    <div class="photo" role="img" aria-label="Tray of chocolate-dipped ice-cream pops with toppings"></div>
  </div>

  <h1 class="welcome">Welcome to our new line of ice-cream desserts</h1>
  <h2 class="try-new">Try our<br>new</h2>

  <div class="product ice-cream">
    <div class="photo" role="img" aria-label="Scoops of chocolate ice-cream"></div>
  </div>
  <div class="product cookie">
    <div class="photo" role="img" aria-label="Cookie ice-cream sandwich slices"></div>
  </div>
  <div class="product cake">
    <div class="photo" role="img" aria-label="Slice of caramel ice-cream cake"></div>
  </div>

  <span class="label ice-cream-label">Ice-cream</span>
  <span class="label cookie-label">Cookie ice-cream</span>
  <span class="label cake-label">Ice-cream cake</span>

  <div class="gold-band bottom">
    <p class="tagline">All hand-made in our kitchen only with natural ingredients</p>
  </div>
</main>
</body>
</html>
```